PowerPoint Template

We would like new powerpoint template for our organization: Fjordvik Data Guild.
Enclosed you find our logo and old template.
Industry/Entity Type
Computer
Requirements
Must have
- 1. Logo
2. Footer (for autor)
3. Font: Variations of ARIAL

```html
<!DOCTYPE html>
<html lang="no">
<head>
<meta charset="utf-8">
<title>Fjordvik Data Guild – presentasjonsmal</title>
<link rel="stylesheet" href="https://fonts.googleapis.com/css2?family=Arimo:wght@400;700&family=Open+Sans:wght@300;400&display=swap">
<style>
:root{
  --ink:#4a4a4a;
  --muted:#8a8a8a;
  --rule:#e6e6e6;
  --band:#13587c;
  --band-text:#b9d3e2;
  --band-link:#2f7aa3;
  --red:#e5414a;
  --blue:#1479c0;
  --green:#138a78;
  --grey-num:#5d5d5d;
  --brown-num:#4b2c2a;
  --item:#f5f5f5;
}
*{margin:0;padding:0;box-sizing:border-box}
html,body{width:1200px;height:900px;overflow:hidden;background:#fff}
body{position:relative;font-family:Arimo,Arial,sans-serif;color:var(--ink)}
.slide{position:absolute;width:600px;height:450px;overflow:hidden}
.slide--welcome{left:0;top:0}
.slide--services{left:600px;top:0}
.slide--about{left:0;top:450px}
.slide--thanks{left:600px;top:450px}
.divider-v{position:absolute;left:600px;top:0;width:1px;height:900px;background:#eee}
.divider-h{position:absolute;left:0;top:450px;width:1200px;height:1px;background:#eee}

.brand{position:absolute;display:flex;flex-direction:column;align-items:flex-start;gap:4px;color:var(--ink);font-weight:700;line-height:1.15}
.brand__square{display:block;background:var(--red)}

.copyright{position:absolute;font-size:4px;color:#777;transform:rotate(-90deg);transform-origin:left top;white-space:nowrap;letter-spacing:.1px}

.welcome__rule{position:absolute;left:222px;top:205px;width:234px;height:1px;background:linear-gradient(90deg,#ddd,#f3f3f3)}
.welcome__title{position:absolute;left:258px;top:197px;font-size:8.5px;letter-spacing:.2px;white-space:nowrap}
.c-green{color:var(--green)} .c-red{color:var(--red)} .c-blue{color:var(--blue)}

.header-bar{position:absolute;height:32px;background:linear-gradient(90deg,#fff,#eee 55%,#fafafa);border-bottom:1px solid #f0f0f0}
.header-bar__title{position:absolute;right:8px;top:2px;font-family:"Open Sans",Arial,sans-serif;font-weight:300;font-size:21px;color:#555;white-space:nowrap}

.service-list{position:absolute;left:205px;top:194px;list-style:none}
.service{display:flex;height:22px;margin-bottom:11px;align-items:stretch}
.service__num{width:30px;color:#fff;font-weight:700;font-size:16px;display:flex;align-items:center;justify-content:center;letter-spacing:-1px}
.service__num--grey{background:var(--grey-num)}
.service__num--brown{background:var(--brown-num)}
.service__label{width:188px;background:var(--item);border:1px solid #eee;font-size:9px;display:flex;align-items:center;padding-left:10px;color:#555;white-space:nowrap}

.footer-band{position:absolute;height:27px;background:var(--band);display:flex;align-items:center;font-size:5.5px}
.footer-band__prev,.footer-band__next{position:absolute;color:var(--band-link);display:flex;align-items:center;gap:1px}
.footer-band__author{position:absolute;left:0;right:0;text-align:center;color:var(--band-text)}

.about__photo{position:absolute;left:116px;top:166px;width:178px;height:68px;background:linear-gradient(120deg,#e9eef2,#c9d3db 45%,#aeb9c3)}
.about__text{position:absolute;font-size:7.2px;line-height:11px;color:#666;text-align:justify}

.thanks__rule{position:absolute;left:195px;top:222px;width:203px;height:1px;background:linear-gradient(90deg,#fff,#ddd,#fff)}
.thanks__title{position:absolute;left:0;width:594px;top:222px;text-align:center;font-size:15px;letter-spacing:-.3px}
</style>
</head>
<body>
<div class="divider-v"></div>
<div class="divider-h"></div>

<section class="slide slide--welcome">
  <div class="brand" style="left:145px;top:186px;width:75px;font-size:12px"><span class="brand__square" style="width:14px;height:14px"></span>Fjordvik<br>Data Guild</div>
  <div class="welcome__rule"></div>
  <p class="welcome__title"><span class="c-green">VELKOMMEN</span> <span class="c-red">TIL DENNE</span> <span class="c-blue">PRESENTASJONEN</span></p>
  <p class="copyright" style="left:566px;top:372px">fjordvikdata.no – 2014, all rights reserved</p>
</section>

<section class="slide slide--services">
  <div class="brand" style="left:123px;top:133px;font-size:7.5px;gap:3px;white-space:nowrap"><span class="brand__square" style="width:10px;height:10px"></span>Fjordvik Data Guild</div>
  <div class="header-bar" style="left:205px;top:128px;width:283px"><h1 class="header-bar__title">Hva gjør vi?</h1></div>
  <ol class="service-list">
    <li class="service"><span class="service__num service__num--grey">01</span><span class="service__label">Markedsfører arrangementer</span></li>
    <li class="service"><span class="service__num service__num--brown">02</span><span class="service__label">Bidrar til å verve medlemmer</span></li>
    <li class="service"><span class="service__num service__num--grey">03</span><span class="service__label">Skaper synlighet i Sosiale Medier</span></li>
    <li class="service"><span class="service__num service__num--brown">04</span><span class="service__label">Bygger merkevare og FDGs omdømme</span></li>
  </ol>
  <footer class="footer-band" style="left:29px;top:369px;width:554px">
    <span class="footer-band__prev" style="left:95px"><svg width="6" height="12" viewBox="0 0 6 12"><path d="M5 1 1 6l4 5" fill="none" stroke="#2f7aa3"/></svg>Previous</span>
    <span class="footer-band__author">Presentation by: Mr. Erik L Strand</span>
    <span class="footer-band__next" style="left:438px">Next<svg width="6" height="12" viewBox="0 0 6 12"><path d="M1 1l4 5-4 5" fill="none" stroke="#2f7aa3"/></svg></span>
  </footer>
  <p class="copyright" style="left:566px;top:366px">fjordvikdata.no – 2014, all rights reserved</p>
</section>

<section class="slide slide--about">
  <div class="brand" style="left:116px;top:87px;font-size:7.5px;gap:3px;white-space:nowrap"><span class="brand__square" style="width:10px;height:10px"></span>Fjordvik Data Guild</div>
  <div class="header-bar" style="left:198px;top:88px;width:290px"><h1 class="header-bar__title" style="font-size:20px">hvem vi er</h1></div>
  <div class="about__photo" role="img" aria-label="Foto: hånd som berører et nettbrett"></div>
  <p class="about__text" style="left:313px;top:172px;width:174px">The FDG is the largest special interest society for information technology (IT) in Norway. It is an open, independent forum for Norway's IT professionals and advanced IT users. The society encompasses the IT industry, corporations in general and research and development institutions.</p>
  <p class="about__text" style="left:116px;top:246px;width:384px;text-align:left;font-size:7px">The FDG is an independent and wholly self-financed society with more than 10,500 registered members and more than 1,200 company members.</p>
  <footer class="footer-band" style="left:18px;top:334px;width:566px">
    <span class="footer-band__prev" style="left:98px"><svg width="6" height="12" viewBox="0 0 6 12"><path d="M5 1 1 6l4 5" fill="none" stroke="#2f7aa3"/></svg>Previous</span>
    <span class="footer-band__author">Presentation by: Mr. Erik L Strand</span>
    <span class="footer-band__next" style="left:448px">Next<svg width="6" height="12" viewBox="0 0 6 12"><path d="M1 1l4 5-4 5" fill="none" stroke="#2f7aa3"/></svg></span>
  </footer>
  <p class="copyright" style="left:566px;top:330px">fjordvikdata.no – 2014, all rights reserved</p>
</section>

<section class="slide slide--thanks">
  <div class="brand" style="left:246px;top:158px;font-size:10px;gap:4px;align-items:center;width:110px;white-space:nowrap"><span class="brand__square" style="width:14px;height:14px"></span>Fjordvik Data Guild</div>
  <div class="thanks__rule"></div>
  <p class="thanks__title"><span class="c-green">takk</span> <span class="c-red">for</span> <span class="c-blue">din tid</span></p>
  <p class="copyright" style="left:566px;top:350px">fjordvikdata.no – 2014, all rights reserved</p>
</section>
</body>
</html>
```